Wellness, Purpose, and the Quiet Path Research Program Website

Overview: This website will serve a new research program (Wellness, Purpose, and the Quiet Path) at the Thornbury University School of Medicine. I want a clean, intuitive design that has a navigation bar, but uses icons/graphic buttons to link to the main pages. In an attached Word document, I have provided a basic information architecture for the site, understanding that this project would just generate graphics and code for the 3 pages. I highlighted the 3 pages I'd like designed.
Target market: People who want to participate in our research, or contribute grant funding to specific projects.
Number of page: The design project focuses on 3 pages, but the site must accommodate 6 pages with top-level links. See attached Word doc.
Logo and website header: Please integrate our logo in the header. I've uploaded it as a png file--both with the name of the website and with just the logo image. I imaging the logo would look great in a banner set against an image of a mountain. The two main design themes I want to see included are nature and healthcare.
Text content: I have not yet provided text. Use some dummy text.
Technical Specifications:
- Build using WordPress. We will host this site ourselves on HostBarrow using WordPress.
- The design package must be coded.
- The template must be responsive to different platforms (e.g., computer, mobile phone, Zelvo).
Thank you! I look forward to seeing your designs.
- Ned

```html
<!DOCTYPE html>
<html lang="en">
<head>
<meta charset="utf-8">
<title>Wellness, Purpose, and the Quiet Path – The Research Program</title>
<link rel="stylesheet" href="https://fonts.googleapis.com/css2?family=Oswald:wght@300;400;500&family=Roboto+Condensed:wght@400;700&family=Open+Sans:wght@400;600&family=Great+Vibes&display=swap">
<style>
:root{
  --blue:#0c5fa8;
  --navy:#123d8c;
  --teal:#0aa58a;
  --green:#0b9a6e;
  --text:#555b61;
  --link:#1d54a0;
  --light:#f1f1f1;
  --panel:#dcdcdc;
  --white:#ffffff;
}
*{margin:0;padding:0;box-sizing:border-box}
html,body{width:1200px;height:2816px;overflow:hidden}
body{position:relative;background:var(--white);font-family:"Open Sans",sans-serif;color:var(--text)}
.abs{position:absolute}

/* hero */
.hero{left:0;top:0;width:1200px;height:600px;background:linear-gradient(180deg,#5b6a7c 0%,#8a7a5c 30%,#6a5a3c 48%,#5d6f78 62%,#4a5a62 100%)}
.hero-edge{left:0;top:570px;width:1200px;height:40px}
.brand{left:50px;top:48px;display:flex;align-items:center;gap:12px}
.brand-dot{width:62px;height:62px;border-radius:50%;background:var(--white);opacity:.9}
.brand-name{font-family:"Open Sans",sans-serif;font-weight:600;font-size:13px;line-height:17px;color:var(--navy);width:290px}
.nav{top:62px;left:600px;display:flex;gap:0}
.nav a{font-family:"Roboto Condensed",sans-serif;font-size:17px;color:var(--white);text-decoration:none;position:absolute;white-space:nowrap;transform:translateX(-50%)}
.hero-rule{left:57px;top:142px;width:1088px;height:1px;background:rgba(255,255,255,.55)}
.hero-sub{left:0;width:1200px;top:274px;text-align:center;font-family:"Oswald",sans-serif;font-weight:300;font-size:33px;color:var(--white)}
.hero-title{left:0;width:1200px;top:312px;text-align:center;font-family:"Oswald",sans-serif;font-weight:500;font-size:54px;color:var(--white);letter-spacing:.5px}
.hero-btn{width:120px;text-align:center;text-decoration:none}
.hero-btn .ring{width:92px;height:92px;margin:0 auto;border:2px solid var(--white);border-radius:50%;background:rgba(255,255,255,.12);display:flex;align-items:center;justify-content:center}
.hero-btn span{display:block;margin-top:10px;font-family:"Roboto Condensed",sans-serif;font-weight:700;font-size:14px;color:var(--white)}

/* people */
.people-block{left:91px;top:847px;width:378px;height:354px;background:linear-gradient(135deg,#0a7a8a,#0b5aa2 60%,#0a9a78)}
.people-frame{left:135px;top:731px;width:410px;height:439px;background:var(--white);box-shadow:0 4px 14px rgba(0,0,0,.18)}
.people-photo{left:145px;top:741px;width:391px;height:419px;background:linear-gradient(160deg,#e8ecef,#c9d4de 40%,#2c5f9a 70%,#dfe5ea)}
.script{font-family:"Great Vibes",cursive;font-size:62px;color:var(--navy);left:573px;top:752px}
.divider{display:flex;align-items:center;gap:10px}
.divider i{display:block;width:34px;height:1px;background:currentColor}
.divider b{display:block;width:14px;height:14px;border-radius:50%;border:2px solid currentColor}
.people-text{left:575px;top:884px;width:540px;font-size:13px;line-height:28px;text-align:justify}
.feature{width:180px;text-align:center;top:1035px}
.feature span{display:block;margin-top:14px;font-family:"Roboto Condensed",sans-serif;font-size:16px;color:#333}

/* research */
.research{left:0;top:1330px;width:1200px;height:548px;background:linear-gradient(90deg,#0d4f9c 0%,#0a6ea0 45%,#0a9a7e 80%,#0b9770 100%)}
.edge{left:0;width:1200px;height:30px}
.research h2{position:absolute;left:0;width:1200px;top:132px;text-align:center;font-family:"Oswald",sans-serif;font-weight:300;font-size:47px;color:var(--white)}
.research .divider{position:absolute;left:560px;top:214px;color:var(--white)}
.research p{position:absolute;left:140px;width:928px;top:260px;text-align:center;font-size:13.5px;line-height:28px;color:var(--white)}
.btn{position:absolute;left:540px;top:398px;width:148px;height:44px;border-radius:22px;background:#0a4fa8;color:var(--white);font-size:13px;line-height:44px;text-align:center;text-decoration:none}

/* faq */
.faq{left:0;top:1878px;width:1200px;height:677px;background:var(--light)}
.faq-art{left:70px;top:2080px;width:370px;height:280px;background:linear-gradient(135deg,#e6f1f7,#d7e9f1 60%,#eef4e0)}
.acc{left:490px;width:647px}
.acc-head{height:58px;background:var(--panel);display:flex;align-items:center;justify-content:space-between;padding:0 18px;font-size:14.5px;color:var(--link)}
.acc-head em{font-style:normal;color:#333}
.acc-head b{font-weight:400;font-size:20px;color:var(--link)}
.acc-body{font-size:15px;line-height:28px;color:var(--link);padding:12px 12px 0}

/* footer */
.footer{left:0;top:2555px;width:1200px;height:198px;background:var(--blue)}
.foot-h{font-family:"Oswald",sans-serif;font-weight:300;font-size:25px;color:var(--white)}
.foot-h strong{font-weight:500}
.email{left:56px;top:2659px;width:250px;height:36px;background:var(--white);border-radius:3px;font-size:14px;color:#777;padding:0 13px;line-height:36px}
.sub-btn{left:311px;top:2658px;width:103px;height:38px;background:var(--teal);color:var(--white);font-family:"Oswald",sans-serif;font-size:15px;text-align:center;line-height:38px;border-radius:3px}
.foot-mark{left:562px;top:2610px;width:110px;text-align:center}
.foot-mark i{display:block;width:60px;height:60px;margin:0 auto 6px;border-radius:50%;border:2px solid var(--white)}
.foot-mark span{font-family:"Open Sans",sans-serif;font-weight:600;font-size:13px;color:var(--white)}
.social{display:flex;gap:10px;left:883px;top:2655px}
.social i{display:block;width:38px;height:38px;border-radius:50%;background:var(--white)}
.bottom{left:0;top:2753px;width:1200px;height:63px;background:var(--teal);color:var(--white);font-size:13.5px}
.crumbs{position:absolute;left:50px;top:22px;display:flex;gap:14px}
.copy{position:absolute;right:55px;top:24px;font-size:13px}
</style>
</head>
<body>

<!-- hero -->
<section class="hero abs" role="img" aria-label="Mountain range rising above a lake at sunset"></section>
<svg class="hero-edge abs" viewBox="0 0 1200 40" preserveAspectRatio="none" aria-hidden="true"><path fill="#fff" d="M0 22 L30 18 L60 24 L95 16 L130 22 L170 15 L210 23 L250 17 L290 21 L330 14 L375 22 L415 16 L460 24 L500 17 L545 21 L590 13 L635 22 L680 17 L720 23 L765 15 L810 21 L855 16 L900 24 L945 17 L990 22 L1035 15 L1080 21 L1125 16 L1165 23 L1200 17 L1200 40 L0 40Z"/></svg>

<header>
  <div class="brand abs"><i class="brand-dot"></i><div class="brand-name">Wellness, Purpose, and the Quiet Path Research Program</div></div>
  <nav class="nav abs" style="left:0;top:62px">
    <a href="#" style="left:637px">Home</a>
    <a href="#" style="left:719px">People</a>
    <a href="#" style="left:813px">Projects</a>
    <a href="#" style="left:899px">FAQ’s</a>
    <a href="#" style="left:983px">Resources</a>
    <a href="#" style="left:1078px">Contact</a>
  </nav>
  <div class="hero-rule abs"></div>
</header>

<div class="hero-sub abs">Wellness, Purpose, and the Quiet Path</div>
<h1 class="hero-title abs">THE RESEARCH PROGRAM</h1>

<a class="hero-btn abs" href="#" style="left:315px;top:415px"><div class="ring"><svg width="46" height="46" viewBox="0 0 46 46" fill="none" stroke="#fff" stroke-width="2"><circle cx="16" cy="12" r="6"/><circle cx="30" cy="12" r="6"/><path d="M6 34 q0-12 10-12 q10 0 10 12M20 34 q0-12 10-12 q10 0 10 12"/></svg></div><span>PEOPLE</span></a>
<a class="hero-btn abs" href="#" style="left:540px;top:415px"><div class="ring"><svg width="48" height="48" viewBox="0 0 48 48" fill="none" stroke="#fff" stroke-width="2"><path d="M4 14 L22 18 L22 38 L4 34Z M22 18 L40 14 L40 34 L22 38"/><circle cx="31" cy="24" r="7"/><path d="M36 29 L44 37"/></svg></div><span>RESEARCH PROJECTS</span></a>
<a class="hero-btn abs" href="#" style="left:762px;top:415px"><div class="ring"><svg width="48" height="48" viewBox="0 0 48 48" fill="none" stroke="#fff" stroke-width="2"><circle cx="19" cy="24" r="12"/><path d="M26 12 a12 10 0 1 1 8 20 l4 6 -8-4"/><path d="M15 21 a4 4 0 1 1 5 4 v3"/><circle cx="20" cy="32" r="1" fill="#fff"/></svg></div><span>FAQ’S</span></a>

<!-- people -->
<div class="people-block abs"></div>
<div class="people-frame abs"></div>
<div class="people-photo abs" role="img" aria-label="Researcher working at a desk with computer and charts, seen from above"></div>
<h2 class="script abs">People</h2>
<div class="divider abs" style="left:590px;top:848px;color:#666"><i></i><b></b><i></i></div>
<p class="people-text abs">Lorem ipsum dolor sit amet, consectetur adipiscing elit. Sed suscipit maximus sapien, ut posuere elit finibus iaculis. Proin elementum magna sit amet risus pulvinar, a efficitur massa fermentum. Praesent ultrices quam in fermentum ultrices. Quisque nibh augue, cursus ac efficitur ut, maximus sit amet orci. Praesent tempus rutrum dignissim...</p>

<a class="feature abs" href="#" style="left:567px;text-decoration:none"><svg width="70" height="70" viewBox="0 0 70 70" fill="none" stroke="#0aa58a" stroke-width="2.5"><circle cx="35" cy="35" r="27" stroke-dasharray="20 8"/><circle cx="35" cy="32" r="11"/><path d="M27 33 h4 l3-6 3 10 3-4 h3"/><circle cx="35" cy="7" r="4" fill="#0aa58a"/><circle cx="12" cy="55" r="4" fill="#0aa58a"/><circle cx="58" cy="55" r="4" fill="#0aa58a"/></svg><span>Research Team</span></a>
<a class="feature abs" href="#" style="left:751px;text-decoration:none"><svg width="76" height="70" viewBox="0 0 76 70" fill="#0aa58a"><ellipse cx="38" cy="34" rx="24" ry="12"/><circle cx="14" cy="22" r="6"/><circle cx="62" cy="22" r="6"/><circle cx="26" cy="14" r="6"/><circle cx="50" cy="14" r="6"/><circle cx="38" cy="11" r="6"/><rect x="6" y="30" width="10" height="18" rx="3"/><rect x="60" y="30" width="10" height="18" rx="3"/></svg><span>Advisory committee</span></a>
<a class="feature abs" href="#" style="left:937px;text-decoration:none"><svg width="76" height="70" viewBox="0 0 76 70" fill="none" stroke="#0aa58a" stroke-width="2.5"><path d="M4 22 L14 12 L24 22 L14 32Z M72 22 L62 12 L52 22 L62 32Z"/><path d="M20 28 L34 48 q4 4 8 0 l14-20"/><path d="M30 24 l10-4 12 6"/><path d="M28 42 l4-4M33 46 l4-4M38 49 l4-4"/></svg><span>Partners</span></a>

<!-- research projects -->
<section class="research abs" role="img" aria-label="Hands writing on research documents, tinted blue and green">
  <h2>Research Projects</h2>
  <div class="divider"><i></i><b></b><i></i></div>
  <p>Aenean efficitur pretium viverra. Aliquam rutrum mauris nunc, et rutrum dolor hendrerit eu. Integer vitae nisi eget enim imperdiet mattis id id sem. Aenean malesuada quis arcu at vulputate. Vivamus tristique, urna aliquam ultricies posuere, est ex aliquet nisl, id malesuada arcu orci vitae sem. Praesent cursus ornare egestas. Donec tempus risus vel est aliquam pharetra.</p>
  <a class="btn" href="#">Read More</a>
</section>
<svg class="edge abs" style="top:1318px" viewBox="0 0 1200 30" preserveAspectRatio="none" aria-hidden="true"><path fill="#fff" d="M0 0 H1200 V18 L1160 12 L1120 20 L1080 13 L1040 19 L1000 12 L960 18 L920 11 L880 19 L840 13 L800 20 L760 12 L720 18 L680 13 L640 20 L600 12 L560 19 L520 13 L480 18 L440 11 L400 19 L360 13 L320 20 L280 12 L240 18 L200 13 L160 20 L120 12 L80 18 L40 13 L0 19Z"/></svg>
<svg class="edge abs" style="top:1858px" viewBox="0 0 1200 30" preserveAspectRatio="none" aria-hidden="true"><path fill="#f1f1f1" d="M0 30 H1200 V12 L1160 18 L1120 10 L1080 17 L1040 11 L1000 18 L960 12 L920 19 L880 11 L840 17 L800 10 L760 18 L720 12 L680 17 L640 10 L600 18 L560 11 L520 17 L480 12 L440 19 L400 11 L360 17 L320 10 L280 18 L240 12 L200 17 L160 10 L120 18 L80 12 L40 17 L0 11Z"/></svg>

<!-- faq -->
<section class="faq abs" aria-label="Frequently asked questions"></section>
<div class="faq-art abs" role="img" aria-label="Illustration of the word FAQ with clouds, speech bubbles and a pencil"></div>

<div class="acc abs" style="top:2035px"><div class="acc-head"><span><em>Q1.</em> What makes this project unique?</span><b>−</b></div></div>
<p class="acc abs acc-body" style="top:2108px">Aenean efficitur pretium viverra. Aliquam rutrum mauris nunc, et rutrum dolor hendrerit eu. Integer vitae nisi eget enim imperdiet mattis id id sem. Aenean malesuada quis arcu at vul-putate.</p>
<div class="acc abs" style="top:2209px"><div class="acc-head"><span>Q2.&nbsp; Does this project assume that the impact of religion is always positive?</span><b>+</b></div></div>
<div class="acc abs" style="top:2286px"><div class="acc-head"><span>Q3.&nbsp; How can I collaborate?</span><b>+</b></div></div>
<div class="acc abs" style="top:2364px"><div class="acc-head"><span>Q4.&nbsp; Will Thornbury faculty lead all projects?</span><b>+</b></div></div>

<!-- footer -->
<footer>
  <div class="footer abs"></div>
  <div class="foot-h abs" style="left:56px;top:2600px">Signup <strong>Newsletter</strong> :</div>
  <div class="email abs">Your Email</div>
  <div class="sub-btn abs">SUBSCRIBE</div>
  <div class="foot-mark abs"><i></i><span>Quiet Path</span></div>
  <div class="foot-h abs" style="left:969px;top:2600px">Stay <strong>In Touch</strong> :</div>
  <div class="social abs" aria-label="Social links"><i></i><i></i><i></i><i></i><i></i></div>
  <div class="bottom abs">
    <div class="crumbs"><span>Home</span><span>/</span><span>People</span><span>/</span><span>Research Projects</span><span>/</span><span>FAQ’s</span><span>/</span><span>Resources</span><span>/</span><span>Contact</span></div>
    <div class="copy">Copyright ©&nbsp; 2010-2021&nbsp; All rights reserved</div>
  </div>
</footer>

</body>
</html>
```